Lawyer health website (wordpress design) to improve well being/health for lawyers

I need a webdesign for personal website called www.plumcounselnest.net. Website will be focused on health/wellness for my profession (lawyers) and other professionals too. Will have a blog on a separate page, a calorie counter on first page, and forums for me to begin topics and users to post. Also want the ability to add and delete information on a consistent basis...especially news articles related to my profession. I will want the homepage to include both health related information - different articles and articles related to the professionl. Need a tab to link my vitabrook site. I like format of www.dailyvigorhub.net and www.nutrimeterplus.net and www.sourcounselor.net. My website will have a mix of these themes and will not be too sarcastic (sourcounselor) but fun and healthy, a place for other attorneys and professionals to go to support eachother in health and wellness and their profession. Will need these things for the website:

(1) Responsive design (can be viewed on mobile phones, ipads, ect.)
(2)Cross browser support
(3) Custom background and colors
(4) Allow admin to post on front end and to add pages and delete and add info
(5) All post will have social media share
(6)Admin can control what is posted on page so if someone comments admin can review it before its posted on articles...forums no control over that. If admin wants to I can change the review function.
(7) Users can sign in with social media accounts or create a user name and password
(8) I am a female attorney so I prefer it be a bit more feminine but I will encourage males to follow the page as well.
(9) Feature attorney of the month or week on a page. I think this would be cool to do on a separate page highlighting an attorney, their practice area, their fitness goals ect.

Target Market(s)

Attorneys

Industry/Entity Type

Health

Coding

Coded - Design and coding required

Number of Pages Required

5+ page

Font styles to use
Serif

Colors
cadf82
85cae6
0355a3
00a990

Requirements
Must have
• Home page with "Featured attorney" section in a corner of page so users can click on that pic to learn about that "Feautured attorney" and how he/she stays fit. Also, calorie counter on home page, blog, Contact Us Page, and Forum Page.
• I MUST HAVE ABILITY TO ADD/DELETE CONTENT ON MY WEBSITE ON A CONSISTENT BASIS.

```html
<!DOCTYPE html>
<html lang="en">
<head>
<meta charset="utf-8">
<title>Plum Counsel Nest — Health &amp; Wellness for Lawyers</title>
<link href="https://fonts.googleapis.com/css2?family=Lato:ital,wght@0,400;0,700;1,400&family=Merriweather:ital,wght@0,700;1,700;1,900&family=Tinos&display=swap" rel="stylesheet">
<style>
:root{
  --lime:#cadf82;
  --sky:#85cae6;
  --navy:#0355a3;
  --teal:#00a990;
  --ink:#333333;
  --body:#444444;
  --muted:#777777;
  --paper:#ffffff;
  --mist:#f0f0f0;
  --footer:#232323;
  --footer-deep:#1d1d1d;
  --footer-text:#9a9a9a;
}
*{box-sizing:border-box;margin:0;padding:0}
html,body{width:906px;height:1200px;overflow:hidden}
body{position:relative;background:var(--paper);font-family:"Lato",sans-serif;color:var(--body)}
.abs{position:absolute}

/* hero */
.hero{position:absolute;left:0;top:0;width:906px;height:424px;overflow:hidden}
.hero-photo{position:absolute;inset:0;
  background:
    radial-gradient(ellipse 340px 200px at 330px 270px, rgba(236,120,190,.85), rgba(236,120,190,0) 70%),
    radial-gradient(ellipse 500px 120px at 620px 400px, rgba(170,110,200,.8), rgba(170,110,200,0) 75%),
    linear-gradient(180deg,#e9e6ea 0%,#efe4ec 40%,#d8b8d8 75%,#b790c9 100%)}
.nav-bar{position:absolute;left:0;top:35px;width:906px;height:35px;background:var(--lime)}
.nav-link{position:absolute;top:45px;font-family:"Tinos",serif;font-size:13px;color:#111;letter-spacing:.3px}
.nav-sep{position:absolute;top:46px;width:1px;height:14px;background:#9fb55a}
.logo{position:absolute;left:99px;top:16px;width:205px;height:70px;background:var(--paper);
  box-shadow:0 1px 4px rgba(0,0,0,.15);display:flex;align-items:center;justify-content:center;gap:7px}
.logo-dot{width:10px;height:10px;border-radius:50%;background:var(--teal)}
.logo-name{font-family:"Merriweather",serif;font-weight:700;font-size:15px;color:#a7c94a}
.search{position:absolute;left:546px;top:6px;width:181px;height:23px;background:rgba(255,255,255,.75);
  border:1px solid #cfcfcf;font-family:"Tinos",serif;font-style:italic;font-size:9px;color:#aaa;padding:6px 6px}
.search svg{position:absolute;right:5px;top:5px}
.login{position:absolute;left:738px;top:5px;width:69px;height:24px;background:var(--sky);color:#fff;
  font-family:"Tinos",serif;font-size:13px;text-align:center;line-height:24px;letter-spacing:.5px;border-radius:2px}
.tagline{position:absolute;left:98px;top:346px;width:390px;height:41px;
  background:linear-gradient(90deg,rgba(133,202,230,.9),rgba(133,202,230,.55) 70%,rgba(133,202,230,0));
  font-family:"Merriweather",serif;font-weight:900;font-style:italic;font-size:20px;color:#fff;
  padding:6px 10px;text-shadow:0 1px 2px rgba(0,0,0,.25)}

/* calorie counter */
.counter{position:absolute;left:581px;top:128px;width:230px;height:243px;background:rgba(96,120,150,.55);border:3px solid rgba(110,120,140,.45)}
.counter-head{height:35px;background:var(--teal);color:#fff;font-family:"Merriweather",serif;font-weight:700;
  font-size:13px;text-align:center;line-height:35px;letter-spacing:.4px}
.field-label{position:absolute;font-size:10px;font-weight:700;color:#fff}
.field{position:absolute;height:26px;background:#fff;border:1px solid #ccc;border-radius:2px;
  font-family:"Lato",sans-serif;font-style:italic;font-size:10px;color:#999;padding:6px 6px}
.field.dark{color:#333}
.spin{position:absolute;right:0;top:0;width:16px;height:24px;border-left:1px solid #ddd}
.go{position:absolute;left:23px;top:195px;width:176px;height:32px;background:var(--teal);color:#fff;
  font-weight:700;font-size:12px;letter-spacing:1px;text-align:center;line-height:32px;border-radius:2px;
  box-shadow:0 2px 2px rgba(0,0,0,.25)}

/* query bar */
.query-bar{position:absolute;left:0;top:424px;width:906px;height:56px;
  background:linear-gradient(180deg,#f3f3f3,#e4e4e4);border-bottom:1px solid #d6d6d6}
.query-text{position:absolute;left:102px;top:442px;font-family:"Merriweather",serif;font-style:italic;font-weight:900;
  font-size:16px;color:var(--navy)}
.query-text .phone{color:var(--teal);font-size:22px}
.cta{position:absolute;left:562px;top:438px;width:245px;height:31px;background:var(--lime);
  font-size:14px;color:var(--teal);text-align:center;line-height:31px;box-shadow:1px 2px 3px rgba(0,0,0,.25)}
.cta b{color:var(--navy)}

/* welcome */
.section-title{position:absolute;font-weight:700;font-size:16px;color:var(--ink)}
.section-title .accent{color:var(--navy)}
.rule{position:absolute;height:1px;background:#dadada}
.rule-mark{position:absolute;height:2px;background:var(--navy)}
.welcome-text{position:absolute;left:99px;top:563px;width:437px;font-size:10.2px;line-height:16px;
  color:var(--body);letter-spacing:.15px;text-align:justify}
.read-more{position:absolute;left:99px;top:670px;width:84px;height:24px;background:var(--teal);color:#fff;
  font-family:"Tinos",serif;font-size:10.5px;text-align:center;line-height:24px;border-radius:2px;letter-spacing:.3px}
.featured{position:absolute;left:562px;top:514px;width:245px;height:192px;background:var(--sky);border:1px solid #5fb1d6}
.featured-title{position:absolute;left:10px;top:11px;font-weight:700;font-size:16px;color:#fff}
.featured-photo{position:absolute;left:12px;top:51px;width:221px;height:125px;border:2px solid #2d86c6;
  background:linear-gradient(90deg,#e8eef2,#cbd6de 40%,#f2f3f4)}

/* news and blog */
.mist{position:absolute;left:0;top:741px;width:906px;height:219px;background:var(--mist)}
.news-row{position:absolute;left:99px;width:347px;height:24px;background:#fff;font-size:10px;color:#333;line-height:24px}
.news-date{position:absolute;left:0;top:0;width:77px;height:24px;background:var(--sky);color:#fff;text-align:center}
.news-head{position:absolute;left:86px;top:0}
.blog-photo{position:absolute;left:477px;top:820px;width:87px;height:101px;border:3px solid #fff;
  background:linear-gradient(180deg,#e3e3e3,#bfb8b2 55%,#3a3a3a)}
.blog-meta{position:absolute;left:584px;top:822px;font-style:italic;font-size:8px;color:var(--teal)}
.blog-title{position:absolute;left:584px;top:840px;font-weight:700;font-size:11px;color:var(--ink)}
.blog-text{position:absolute;left:584px;top:856px;width:225px;font-size:10px;line-height:16px;color:var(--muted)}
.blog-text a{color:var(--navy);text-decoration:none}

/* footer */
.footer{position:absolute;left:0;top:960px;width:906px;height:138px;background:var(--footer)}
.footer-title{position:absolute;top:983px;font-size:13px;color:#fff}
.footer-text{position:absolute;font-size:10px;line-height:18px;color:var(--footer-text)}
.footer-text b{color:#fff}
.footer-divider{position:absolute;top:981px;width:1px;height:99px;background:#444}
.newsletter{position:absolute;left:347px;top:1020px;width:214px;height:32px;border:1px solid #444;
  font-size:10px;color:var(--footer-text);padding:9px 12px}
.newsletter svg{position:absolute;right:12px;top:11px}
.footer-bottom{position:absolute;left:0;top:1098px;width:906px;height:102px;background:var(--footer-deep);border-top:1px solid #333}
.bottom-nav{position:absolute;left:0;top:1112px;width:906px;text-align:center;font-size:10.5px;color:var(--footer-text);word-spacing:2px}
.bottom-nav span{margin:0 8px}
.social{position:absolute;top:1141px;width:18px;height:18px;border-radius:50%;background:#555}
.social.active{background:var(--sky)}
.copyright{position:absolute;left:0;top:1175px;width:906px;text-align:center;font-size:10px;color:var(--footer-text)}
</style>
</head>
<body>

<header class="hero">
  <div class="hero-photo" role="img" aria-label="Photo of a smiling woman in a pink top doing sit-ups on an exercise mat in a bright gym"></div>
  <div class="nav-bar"></div>
  <span class="nav-link" style="left:328px">HOME</span>
  <span class="nav-sep" style="left:386px"></span>
  <span class="nav-link" style="left:406px">FEATURED ATTORNEY</span>
  <span class="nav-sep" style="left:565px"></span>
  <span class="nav-link" style="left:586px">BLOG</span>
  <span class="nav-sep" style="left:642px"></span>
  <span class="nav-link" style="left:662px">FORUM</span>
  <span class="nav-sep" style="left:728px"></span>
  <span class="nav-link" style="left:748px">CONTACT</span>

  <div class="logo"><span class="logo-dot"></span><span class="logo-name">Plum Counsel Nest</span></div>

  <div class="search">SEARCH
    <svg width="12" height="12" viewBox="0 0 12 12"><circle cx="5" cy="5" r="3.8" fill="none" stroke="#555" stroke-width="1.4"/><line x1="8" y1="8" x2="11" y2="11" stroke="#555" stroke-width="1.5"/></svg>
  </div>
  <div class="login">LOGIN</div>

  <div class="tagline">Best way to lose your weight</div>

  <div class="counter">
    <div class="counter-head">CALORIE COUNTER</div>
    <span class="field-label" style="left:23px;top:48px">HIGHT</span>
    <div class="field" style="left:24px;top:61px;width:86px">ft<span class="spin"><svg width="16" height="24" viewBox="0 0 16 24"><path d="M5 10l3-3 3 3M5 14l3 3 3-3" fill="none" stroke="#777" stroke-width="1"/></svg></span></div>
    <div class="field" style="left:117px;top:61px;width:85px">in<span class="spin"><svg width="16" height="24" viewBox="0 0 16 24"><path d="M5 10l3-3 3 3M5 14l3 3 3-3" fill="none" stroke="#777" stroke-width="1"/></svg></span></div>
    <span class="field-label" style="left:24px;top:97px">WEIGHT</span>
    <span class="field-label" style="left:118px;top:97px">AGE</span>
    <div class="field" style="left:24px;top:111px;width:86px">lbs<span class="spin"><svg width="16" height="24" viewBox="0 0 16 24"><path d="M5 10l3-3 3 3M5 14l3 3 3-3" fill="none" stroke="#777" stroke-width="1"/></svg></span></div>
    <div class="field" style="left:117px;top:111px;width:85px"><span class="spin"><svg width="16" height="24" viewBox="0 0 16 24"><path d="M5 10l3-3 3 3M5 14l3 3 3-3" fill="none" stroke="#777" stroke-width="1"/></svg></span></div>
    <span class="field-label" style="left:23px;top:145px">GENDER</span>
    <div class="field dark" style="left:24px;top:158px;width:179px">Female<span class="spin" style="width:20px"><svg width="20" height="24" viewBox="0 0 20 24"><path d="M7 11l3 3 3-3" fill="none" stroke="#777" stroke-width="1"/></svg></span></div>
    <div class="go">GO</div>
  </div>
</header>

<section class="query-bar"></section>
<p class="query-text">For any query call us on - <span class="phone">555-210-4836</span></p>
<div class="cta">Click here to visit our <b>Vitabrook</b> site</div>

<main>
  <h2 class="section-title" style="left:99px;top:523px"><span class="accent">WELCOME TO</span> PLUM COUNSEL NEST</h2>
  <div class="rule" style="left:99px;top:549px;width:437px"></div>
  <div class="rule-mark" style="left:99px;top:548px;width:106px"></div>
  <p class="welcome-text">Lorem ipsum dolor sit amet, consectetur adipiscing elit. Aenean sodales diam quis velit pellentesque vehicula. Donec luctus justo aliquet est volutpat, sed tincidunt odio pretium. Sed id est ultrici rutrum arcu pretium, porttitor enim. Integer quis luctus ligula. Donec id scelerisque lorem. Duis vehicu nulla at tristique semper. Vivamus id volutpat ipsum, eget fermentum nunc. Aenean eu semper m Maecenas tellus lacus, elementum vitae fringilla eget, lobortis at sapien. Nullam pharetraluctus ligula. Donec id scelerisque lorem.</p>
  <div class="read-more">READ MORE</div>

  <aside class="featured">
    <h2 class="featured-title">FEATURED ATTORNEY</h2>
    <div class="rule" style="left:10px;top:35px;width:224px;background:#5aa6cc"></div>
    <div class="rule-mark" style="left:10px;top:34px;width:72px"></div>
    <div class="featured-photo" role="img" aria-label="Portrait photo of the featured attorney in a bright office"></div>
  </aside>

  <section class="mist"></section>

  <h2 class="section-title" style="left:98px;top:772px"><span class="accent">LATEST</span> NEWS</h2>
  <div class="rule" style="left:98px;top:801px;width:348px"></div>
  <div class="rule-mark" style="left:98px;top:800px;width:72px"></div>
  <div class="news-row" style="top:818px"><span class="news-date">10-July-2014</span><span class="news-head">Ut wisi enim ad mm ve nostrud exerci tatixerci tation.</span></div>
  <div class="news-row" style="top:846px"><span class="news-date">09-July-2014</span><span class="news-head">Lorem ipsum dolor sit amet,ectetuer adipiscing elit.</span></div>
  <div class="news-row" style="top:873px"><span class="news-date">08-July-2014</span><span class="news-head">Ut wisi enim ad &nbsp;adipiscinin sed m inmnonummy nibh.</span></div>
  <div class="news-row" style="top:901px"><span class="news-date">07-July-2014</span><span class="news-head">Ut wisi enim ad minis nou twmatio nexerci tation.</span></div>

  <h2 class="section-title" style="left:475px;top:772px"><span class="accent">LATEST</span> BLOG</h2>
  <div class="rule" style="left:475px;top:801px;width:332px"></div>
  <div class="rule-mark" style="left:475px;top:800px;width:70px"></div>
  <div class="blog-photo" role="img" aria-label="Photo of a smiling woman in a dark business jacket"></div>
  <p class="blog-meta">By John &nbsp;| &nbsp;7 Hours Ago &nbsp;| &nbsp;In: Funny, Owned, Tech, Too True</p>
  <p class="blog-title">Lorem ipsum dolor sit amet, consectetung</p>
  <p class="blog-text">elit, sed diam nonummy nibh euismod tincidunt ut laoreet dolore magna aliquam erat volut wisi enim ad minim veniam, quis nostrud exerci ullamcorper suscipit lobortis nisl. <a href="#">Read More</a></p>
</main>

<footer>
  <div class="footer"></div>
  <h3 class="footer-title" style="left:101px">PLUM COUNSEL NEST</h3>
  <p class="footer-text" style="left:100px;top:1005px;width:200px">000 Vestibulum suscipit tellus fermentum nibh blandit congue In ipsum pretium suscipit ut quam.<br>000 000</p>
  <div class="footer-divider" style="left:318px"></div>
  <h3 class="footer-title" style="left:371px">SIGN UP FOR NEWSLETTER</h3>
  <div class="newsletter">Enter your email here
    <svg width="9" height="9" viewBox="0 0 9 9"><path d="M0 4.5h7M4.5 1.5l3 3-3 3" fill="none" stroke="#ccc" stroke-width="1.2"/></svg>
  </div>
  <div class="footer-divider" style="left:590px"></div>
  <h3 class="footer-title" style="right:100px">REACH US</h3>
  <p class="footer-text" style="right:100px;top:1005px;text-align:right"><b>m</b>: (555) 304 7712<br>(555) 304 7712<br><b>o</b>: (555) 304 7712<br><b>e</b>: info@plumcounselnest.net</p>

  <div class="footer-bottom"></div>
  <nav class="bottom-nav"><span>HOME</span>|<span>FEATURED ATTORNEY</span>|<span>BLOG</span>|<span>FORUM</span>|<span>CONTACT</span></nav>
  <span class="social active" style="left:405px"></span>
  <span class="social" style="left:431px"></span>
  <span class="social" style="left:457px"></span>
  <span class="social" style="left:482px"></span>
  <p class="copyright">© 2015 PLUM COUNSEL NEST | &nbsp;All Rights reserved.</p>
</footer>

</body>
</html>
```